Lantern Business Cards

Need business cards for my employees at my restaurant.

Needs to include:
Our Logo
Lantern Bowls & Brews
Name: Nora Pettigrew
Title : Owner
Address: 487 Mirella Ave. Kestrel Bay City, NV 86519
Web: www.lanternkestrel.com
Phone: 928-555-0147
Cell: 928-555-0192
Email: info@lanternkestrel.com

```html
<!DOCTYPE html>
<html lang="en">
<head>
<meta charset="utf-8">
<title>Lantern Bowls &amp; Brews – Business Cards</title>
<link rel="stylesheet" href="https://fonts.googleapis.com/css2?family=Poppins:wght@300;400;600;700&display=swap">
<style>
  :root {
    --canvas: #2b2b2d;
    --card: #1d1d1f;
    --brand-red: #c3202f;
    --ink-light: #f2f2f2;
    --pattern-light: #5a5a5c;
    --pattern-dark: #121213;
  }
  * { box-sizing: border-box; margin: 0; padding: 0; }
  html, body { width: 1200px; height: 758px; overflow: hidden; }
  body {
    background: var(--canvas);
    font-family: "Poppins", sans-serif;
    display: flex;
    align-items: center;
    justify-content: center;
    gap: 40px;
  }
  .card {
    position: relative;
    width: 550px;
    height: 314px;
    border-radius: 18px;
    background: var(--card);
    overflow: hidden;
    box-shadow: 0 10px 30px rgba(0,0,0,.45);
  }

  /* Front */
  .card-front__pattern {
    position: absolute; inset: 0;
    background: linear-gradient(115deg, var(--pattern-light) 0%, #3a3a3c 35%, #1f1f21 65%, var(--pattern-dark) 100%);
  }
  .card-front__brand {
    position: absolute;
    left: 50%; top: 50%;
    transform: translate(-50%, -50%);
    display: flex;
    align-items: center;
    gap: 14px;
  }
  .brand-dot {
    width: 46px; height: 46px;
    border-radius: 50%;
    background: var(--ink-light);
    flex: none;
  }
  .wordmark { display: flex; flex-direction: column; }
  .wordmark__name {
    font-weight: 700;
    color: var(--brand-red);
    line-height: 1;
    letter-spacing: 1px;
    text-transform: uppercase;
  }
  .wordmark__tagline {
    display: flex; align-items: center; gap: 8px;
    color: var(--ink-light);
    font-weight: 400;
    text-transform: uppercase;
    letter-spacing: 1.6px;
    margin-top: 6px;
  }
  .wordmark__tagline::before,
  .wordmark__tagline::after {
    content: ""; height: 1px; background: var(--ink-light); flex: 1;
  }
  .card-front .wordmark__name { font-size: 40px; }
  .card-front .wordmark__tagline { font-size: 9px; }

  /* Back */
  .card-back__accent {
    position: absolute; right: 0; top: 28px;
    width: 9px; height: 40px;
    background: var(--brand-red);
  }
  .card-back__person {
    position: absolute; right: 26px; top: 26px;
    text-align: right;
  }
  .person__name {
    font-size: 19px; font-weight: 700;
    color: var(--brand-red);
    letter-spacing: .8px;
    text-transform: uppercase;
    line-height: 1.1;
  }
  .person__title {
    font-size: 11px; font-weight: 400;
    color: var(--ink-light);
    letter-spacing: 1px;
    text-transform: uppercase;
  }
  .card-back__mark {
    position: absolute; right: 24px; top: 92px;
    width: 190px; height: 190px;
    border-radius: 14px;
    background: radial-gradient(circle at 40% 40%, #333335 0%, #242426 60%, var(--card) 100%);
  }
  .card-back .wordmark {
    position: absolute; left: 38px; top: 96px;
  }
  .card-back .wordmark__name { font-size: 44px; }
  .card-back .wordmark__tagline { font-size: 9.5px; }
  .contact {
    position: absolute; left: 44px; top: 184px;
    color: var(--ink-light);
    font-size: 12px; font-weight: 400;
    line-height: 1.55;
  }
  .contact__address { margin-left: 20px; margin-bottom: 4px; }
  .contact__list { list-style: none; }
  .contact__item { display: flex; align-items: center; gap: 8px; }
  .contact__icon { width: 12px; height: 12px; fill: var(--brand-red); flex: none; }
</style>
</head>
<body>

  <section class="card card-front" aria-label="Card front">
    <div class="card-front__pattern" role="img" aria-label="Embossed repeating brand pattern on black, glossy fading from grey to black"></div>
    <div class="card-front__brand">
      <span class="brand-dot"></span>
      <div class="wordmark">
        <span class="wordmark__name">Lantern</span>
        <span class="wordmark__tagline">Bowls and Brews</span>
      </div>
    </div>
  </section>

  <section class="card card-back" aria-label="Card back">
    <span class="card-back__accent"></span>
    <div class="card-back__person">
      <p class="person__name">Nora Pettigrew</p>
      <p class="person__title">Owner</p>
    </div>

    <div class="card-back__mark" role="img" aria-label="Large embossed brand symbol in dark grey"></div>

    <div class="wordmark">
      <span class="wordmark__name">Lantern</span>
      <span class="wordmark__tagline">Bowls and Brews</span>
    </div>

    <div class="contact">
      <p class="contact__address">487 Mirella Ave.<br>Kestrel Bay City, NV 86519</p>
      <ul class="contact__list">
        <li class="contact__item">
          <svg class="contact__icon" viewBox="0 0 24 24" aria-hidden="true"><path d="M6.6 10.8a15.1 15.1 0 0 0 6.6 6.6l2.2-2.2c.3-.3.7-.4 1-.2 1.1.4 2.3.6 3.6.6.6 0 1 .4 1 1V20c0 .6-.4 1-1 1A17 17 0 0 1 3 4c0-.6.4-1 1-1h3.5c.6 0 1 .4 1 1 0 1.3.2 2.5.6 3.6.1.3 0 .7-.2 1z"/></svg>
          <span>928-555-0147</span>
        </li>
        <li class="contact__item">
          <svg class="contact__icon" viewBox="0 0 24 24" aria-hidden="true"><path d="M7 1h10a2 2 0 0 1 2 2v18a2 2 0 0 1-2 2H7a2 2 0 0 1-2-2V3a2 2 0 0 1 2-2zm0 3v14h10V4zm5 15.5a1 1 0 1 0 0 2 1 1 0 0 0 0-2z"/></svg>
          <span>928-555-0192</span>
        </li>
        <li class="contact__item">
          <svg class="contact__icon" viewBox="0 0 24 24" aria-hidden="true"><path d="M2 5h20v14H2zm2 2v.5l8 5 8-5V7zm0 2.9V17h16V9.9l-8 5z"/></svg>
          <span>info@lanternkestrel.com</span>
        </li>
        <li class="contact__item">
          <svg class="contact__icon" viewBox="0 0 24 24" aria-hidden="true"><path d="M12 2a10 10 0 1 0 0 20 10 10 0 0 0 0-20zm-1 17.9A8 8 0 0 1 4.1 10L9 15v1c0 1.1.9 2 2 2zm6.9-2.5c-.3-.8-1-1.4-1.9-1.4h-1v-3c0-.6-.4-1-1-1H8v-2h2c.6 0 1-.4 1-1V7h2a2 2 0 0 0 2-2v-.4a8 8 0 0 1 2.9 12.8z"/></svg>
          <span>www.lanternkestrel.com</span>
        </li>
      </ul>
    </div>
  </section>

</body>
</html>
```